Thrive Hollow Wording For Logo & Business card

I have the logo, I just need the "thrive Hollow" wording to go with it, and a business card design. The only thing on the business card is the website info. We provide nature connection experiences, and bolster these efforts through writing and host a platform for community around it.

I also have an idea of what it could look like (sketch), though I'm really not sure how it would come out. I am open to the best design and happy to consider original artwork. You can see what the site is about at ThriveHollow.com.

Contact Information for Business Card

The only thing on the business card is the website info and the design. I will put other messaging on the back.

Website lettering (ThriveHollow.com) in Montserrat

Logo Text

Thrive Hollow (letters optional)

Font styles to use
Other font styles liked:
• montserrat

```html
<!DOCTYPE html>
<html lang="en">
<head>
<meta charset="utf-8">
<title>Thrive Hollow – Business Card</title>
<link rel="stylesheet" href="https://fonts.googleapis.com/css2?family=Montserrat:wght@400;500;600&display=swap">
<style>
  :root {
    --page: #d9d9dc;
    --purple-deep: #13072a;
    --purple-mid: #2b1640;
    --purple-light: #56305f;
    --orange: #f07d10;
    --white: #ffffff;
    --paper: #efeef2;
    --burst: #f5ece2;
    --logo-grey: #d7d6da;
  }
  * { box-sizing: border-box; margin: 0; padding: 0; }
  html, body {
    width: 1200px; height: 800px; overflow: hidden;
    background: var(--page);
    font-family: "Montserrat", Arial, sans-serif;
  }
  .stage {
    width: 1200px; height: 800px;
    display: flex; align-items: center; justify-content: center; gap: 40px;
  }
  .card {
    position: relative; width: 540px; height: 309px;
    border-radius: 22px; overflow: hidden;
    box-shadow: 0 12px 28px rgba(0,0,0,.22);
  }

  /* Front */
  .card-front {
    background: linear-gradient(20deg, var(--purple-deep) 0%, var(--purple-mid) 55%, var(--purple-light) 100%);
  }
  .front-light {
    position: absolute; inset: 0;
    background: var(--paper);
    clip-path: polygon(62% 0, 100% 0, 100% 100%, 90% 100%);
  }
  .burst-area {
    position: absolute; left: 240px; top: 20px; width: 270px; height: 270px;
    border-radius: 50%;
    background: radial-gradient(circle, #fff7ea 0%, var(--burst) 55%, #f3c48f 100%);
    border: 3px solid var(--orange);
  }
  .front-logo {
    position: absolute; left: 240px; top: 20px; width: 270px; height: 270px;
    display: flex; align-items: center; justify-content: center; gap: 8px;
  }
  .logo-dot {
    width: 18px; height: 18px; border-radius: 50%; background: var(--orange);
  }
  .front-logo .logo-name {
    font-weight: 600; font-size: 24px; color: var(--purple-deep); letter-spacing: .5px;
  }
  .front-web {
    position: absolute; left: 34px; bottom: 40px; width: 200px;
  }
  .zigzag { display: block; margin: 0 0 10px; }
  .front-web .url { color: var(--orange); font-size: 14px; font-weight: 400; }

  /* Back */
  .card-back {
    background: linear-gradient(20deg, var(--purple-deep) 0%, var(--purple-mid) 50%, var(--purple-light) 100%);
  }
  .back-logo {
    position: absolute; left: 0; right: 0; top: 92px;
    display: flex; align-items: center; justify-content: center; gap: 12px;
  }
  .back-logo .logo-dot { width: 30px; height: 30px; }
  .back-logo .logo-name {
    font-weight: 600; font-size: 42px; color: var(--logo-grey); letter-spacing: 1px;
  }
  .back-web {
    position: absolute; left: 20px; right: 20px; top: 200px;
    display: flex; align-items: center; gap: 12px;
  }
  .back-web .rule { flex: 1; height: 10px; }
  .back-web .url { color: var(--white); font-size: 16px; letter-spacing: 1.5px; }
</style>
</head>
<body>
<main class="stage">

  <section class="card card-front">
    <div class="front-light"></div>
    <div class="burst-area" role="img" aria-label="Sunburst ornament framing the brand mark"></div>
    <div class="front-logo">
      <span class="logo-dot"></span>
      <span class="logo-name">Thrive Hollow</span>
    </div>

    <div class="front-web">
      <svg class="zigzag" width="120" height="8" viewBox="0 0 120 8"><polyline points="0,6 8,2 16,6 24,2 32,6 40,2 48,6 56,2 64,6 72,2 80,6 88,2 96,6 104,2 112,6 120,2" fill="none" stroke="#f07d10" stroke-width="1.2"/></svg>
      <p class="url">www.ThriveHollow.com</p>
    </div>
  </section>

  <section class="card card-back">
    <div class="back-logo">
      <span class="logo-dot"></span>
      <span class="logo-name">Thrive Hollow</span>
    </div>
    <div class="back-web">
      <svg class="rule" viewBox="0 0 160 10" preserveAspectRatio="none"><polyline points="0,8 8,2 16,8 24,2 32,8 40,2 48,8 56,2 64,8 72,2 80,8 88,2 96,8 104,2 112,8 120,2 128,8 136,2 144,8 152,2 160,8" fill="none" stroke="#f07d10" stroke-width="1.2" vector-effect="non-scaling-stroke"/></svg>
      <span class="url">www.ThriveHollow.com</span>
      <svg class="rule" viewBox="0 0 160 10" preserveAspectRatio="none"><polyline points="0,8 8,2 16,8 24,2 32,8 40,2 48,8 56,2 64,8 72,2 80,8 88,2 96,8 104,2 112,8 120,2 128,8 136,2 144,8 152,2 160,8" fill="none" stroke="#f07d10" stroke-width="1.2" vector-effect="non-scaling-stroke"/></svg>
    </div>
  </section>

</main>
</body>
</html>
```